Handyman business card & stationary
Your Home Maintenance Specialist
Handyman business card & stationary - Construction
Creative Brief
Bright & Fun-filled
Marv Dobrinski
Owner
4837 Harbrook Lane Brenford, Texas 75321
Marv@steadfixrepairs.com
steadfixrepairs.com
Bonded and Insured
Your Home Maintenance Specialist Call of for a free estimate 469-381-7042

```html
<!DOCTYPE html>
<html lang="en">
<head>
<meta charset="utf-8">
<title>Steadfix Repairs – Business Card</title>
<link rel="stylesheet" href="https://fonts.googleapis.com/css2?family=Open+Sans:wght@400;600;700&family=Oswald:wght@400;500&display=swap">
<style>
  :root {
    --stage: #d9dadb;
    --navy: #2b2a78;
    --navy-deep: #25246a;
    --brand-blue: #2f4fa8;
    --accent-red: #d63a3f;
    --ink: #3a3f55;
    --paper: #ffffff;
    --soft-white: #e9e9f5;
  }
  * { box-sizing: border-box; margin: 0; padding: 0; }
  html, body { width: 1200px; height: 857px; overflow: hidden; }
  body {
    background: var(--stage);
    font-family: "Open Sans", Arial, sans-serif;
    position: relative;
  }
  .card {
    position: absolute;
    width: 540px;
    height: 309px;
    border-bottom: 4px solid var(--accent-red);
    box-shadow: 0 6px 18px rgba(0,0,0,0.18);
  }
  /* Front */
  .card-front { left: 40px; top: 250px; background: var(--paper); color: var(--ink); }
  .card-front .brand {
    position: absolute; left: 34px; top: 150px;
    display: flex; align-items: center; gap: 8px;
  }
  .brand-square { width: 14px; height: 14px; background: var(--accent-red); }
  .brand-name {
    font-family: "Open Sans", Arial, sans-serif; font-weight: 700;
    font-size: 20px; color: var(--brand-blue); letter-spacing: 0.5px;
    white-space: nowrap;
  }
  .card-front .owner {
    position: absolute; right: 34px; top: 62px; text-align: right;
  }
  .owner-name { font-size: 18px; font-weight: 700; color: var(--brand-blue); }
  .card-front .rule {
    position: absolute; left: 34px; right: 34px; top: 112px;
    height: 2px; background: var(--brand-blue);
  }
  .card-front .contacts {
    position: absolute; left: 320px; top: 150px;
    font-size: 11px; line-height: 22px;
  }
  .contact { display: flex; align-items: center; gap: 7px; white-space: nowrap; }
  .contact svg { width: 12px; height: 12px; fill: var(--brand-blue); }
  .card-front .address {
    position: absolute; left: 34px; top: 210px; font-size: 11px; line-height: 16px;
  }
  .card-front .site {
    position: absolute; left: 34px; bottom: 20px; font-size: 11px; color: var(--brand-blue);
  }
  /* Back */
  .card-back {
    left: 620px; top: 300px;
    background: linear-gradient(160deg, var(--navy) 0%, var(--navy-deep) 100%);
    color: var(--soft-white);
    display: flex; flex-direction: column; align-items: center; justify-content: center;
    text-align: center;
  }
  .card-back .brand-faint {
    font-weight: 700; font-size: 22px; color: rgba(255,255,255,0.22); letter-spacing: 0.5px;
    margin-bottom: 18px;
  }
  .card-back .slogan { font-size: 13px; line-height: 19px; }
  .card-back .phone {
    font-family: "Oswald", Arial, sans-serif; font-weight: 500;
    font-size: 38px; color: var(--paper); margin-top: 10px; letter-spacing: 1px;
  }
</style>
</head>
<body>
  <section class="card card-front">
    <div class="owner">
      <div class="owner-name">Marv Dobrinski</div>
    </div>
    <div class="rule"></div>
    <div class="brand">
      <span class="brand-square"></span>
      <span class="brand-name">STEADFIX REPAIRS</span>
    </div>
    <div class="contacts">
      <div class="contact">
        <svg viewBox="0 0 24 24"><path d="M6.6 10.8a15.1 15.1 0 0 0 6.6 6.6l2.2-2.2a1 1 0 0 1 1-.25 11.4 11.4 0 0 0 3.6.57 1 1 0 0 1 1 1V20a1 1 0 0 1-1 1A17 17 0 0 1 3 4a1 1 0 0 1 1-1h3.5a1 1 0 0 1 1 1c0 1.25.2 2.45.57 3.57a1 1 0 0 1-.25 1z"/></svg>
        <span>469-381-7042</span>
      </div>
      <div class="contact">
        <svg viewBox="0 0 24 24"><path d="M2 5h20v14H2zm2 2v.5l8 5 8-5V7zm0 2.9V17h16V9.9l-8 5z"/></svg>
        <span>Marv@steadfixrepairs.com</span>
      </div>
    </div>
    <div class="address">4837 Harbrook Lane<br>Brenford, Texas 75321</div>
    <div class="site">steadfixrepairs.com</div>
  </section>

  <section class="card card-back">
    <div class="brand-faint">STEADFIX REPAIRS</div>
    <div class="slogan">Your Home Maintenance Specialist<br>Call of for a free estimate</div>
    <div class="phone">469-381-7042</div>
  </section>
</body>
</html>
```